Design required for boutique fire engineering firm in New Zealand

Our website was published based on free Wordpress templates, we'd like something a bit more bespoke, clean and simple.

Reason: didn't check this finished on a Sunday :)

Target Market(s)

architects, building owners, property developers

Industry/Entity Type

Boutique

Contact Information for Business Card

Logo
Fire Engineering

Derek Holloway
Principal
+64 21 738 152
derek@veltraxa.nz
veltraxa.nz

Number of Pages Required

3 page

Font styles to use
Sans Serif

Requirements
Nice to have
• On the business card, an embossed logo would be great - not sure if that's a design thing or just a print thing?
• Website, existing @ http://veltraxa.nz for extent of content and general arrangement that I'm happy with.
• Ability to update the content with project bio's and some photos at a later date would be nice.

```html
<!DOCTYPE html>
<html lang="en">
<head>
<meta charset="utf-8">
<title>Veltraxa — Home Page Design</title>
<link rel="stylesheet" href="https://fonts.googleapis.com/css2?family=Montserrat:wght@800;900&family=Nunito+Sans:ital,wght@0,300;0,400;0,600;0,700;1,300;1,400&display=swap">
<style>
  :root {
    --page: #ffffff;
    --screen: #151314;
    --ink: #ffffff;
    --muted: #cfcfcf;
    --soft: #bdbdbd;
    --ember: #f07a0a;
    --ember-deep: #b5480a;
    --footer: rgba(8, 6, 6, 0.62);
    --label: #e0261c;
    --board-title: #151314;
  }
  * { box-sizing: border-box; margin: 0; padding: 0; }
  html, body {
    width: 1200px; height: 1200px; overflow: hidden;
    background: var(--page);
    font-family: "Nunito Sans", Arial, sans-serif;
  }
  .board { position: relative; width: 1200px; height: 1200px; }

  .page-title {
    position: absolute; left: 1103px; top: 22px;
    width: 70px; height: 310px;
    display: flex; align-items: center; justify-content: center;
  }
  .page-title span {
    display: block; transform: rotate(90deg);
    font-family: "Montserrat", Arial, sans-serif; font-weight: 900;
    font-size: 92px; line-height: 1; letter-spacing: 2px;
    color: var(--board-title); white-space: nowrap;
  }

  .state-label {
    position: absolute; left: 122px; width: 952px;
    text-align: center; color: var(--label);
    font-family: "Nunito Sans", Arial, sans-serif; font-weight: 400;
    font-size: 26px; letter-spacing: 0.5px; line-height: 1;
  }
  .state-label--inactive { top: 570px; }
  .state-label--active { top: 1150px; }

  .screen {
    position: absolute; left: 122px; width: 952px; height: 535px;
    background: var(--screen); overflow: hidden; color: var(--ink);
  }
  .screen--inactive { top: 30px; }
  .screen--active { top: 610px; }

  .screen__glow {
    position: absolute; left: 0; top: 0; width: 100%; height: 100%;
    background:
      radial-gradient(ellipse 330px 210px at 50% 470px, rgba(240,122,10,0.95) 0%, rgba(214,96,10,0.7) 35%, rgba(150,55,10,0.35) 65%, rgba(21,19,20,0) 100%),
      radial-gradient(ellipse 520px 330px at 50% 470px, rgba(181,72,10,0.55) 0%, rgba(100,40,12,0.25) 55%, rgba(21,19,20,0) 100%);
  }

  .brand {
    position: absolute; left: 20px; top: 17px;
    display: flex; align-items: center; gap: 10px;
  }
  .brand__mark {
    width: 46px; height: 46px; border-radius: 50%;
    border: 4px solid var(--ink);
  }
  .brand__name {
    font-family: "Nunito Sans", Arial, sans-serif; font-weight: 700;
    font-size: 36px; line-height: 1; color: var(--ink); letter-spacing: -0.5px;
  }

  .nav {
    position: absolute; top: 27px; right: 58px;
    display: flex; gap: 51px;
  }
  .nav__link {
    font-size: 14px; font-weight: 400; letter-spacing: 0.3px;
    color: var(--ink); text-decoration: none;
  }

  .hero {
    position: absolute; left: 0; top: 190px; width: 100%;
    text-align: center;
  }
  .hero__title {
    font-family: "Montserrat", Arial, sans-serif; font-weight: 900;
    font-size: 55px; line-height: 1; letter-spacing: 0.5px; color: var(--ink);
  }
  .hero__subtitle {
    margin-top: 8px;
    font-size: 18px; font-weight: 300; letter-spacing: 0.3px;
    color: var(--muted);
  }
  .hero__cta {
    display: inline-block; margin-top: 23px;
    width: 160px; height: 38px; line-height: 34px;
    border: 2px solid var(--ink); border-radius: 4px;
    font-size: 13.5px; font-weight: 400; letter-spacing: 0.3px;
    color: var(--ink); text-decoration: none; background: transparent;
    position: relative;
  }
  .screen--active .hero__cta { background: #000000; }
  .hero__pointer {
    position: absolute; left: 104px; top: 24px; width: 12px; height: 16px;
  }

  .tagline {
    position: absolute; left: 0; top: 401px; width: 100%;
    text-align: center; font-style: italic; font-weight: 300;
    font-size: 13.5px; color: var(--soft); letter-spacing: 0.2px;
  }

  .site-footer {
    position: absolute; left: 0; top: 458px; width: 100%; height: 77px;
    background: var(--footer);
  }
  .site-footer__legal {
    position: absolute; left: 21px; top: 50px;
    font-size: 11.5px; color: var(--ink); font-weight: 400;
  }
  .site-footer__legal em { font-style: italic; }
  .site-footer__legal a { color: var(--ember); text-decoration: none; }
  .social {
    position: absolute; right: 23px; top: 14px; text-align: center;
  }
  .social__caption { font-size: 9.5px; color: var(--muted); margin-left: 8px; }
  .social__list {
    display: flex; gap: 13px; margin-top: 8px; list-style: none;
  }
  .social__item {
    width: 25px; height: 25px; border-radius: 50%; background: var(--ink);
  }
</style>
</head>
<body>
<main class="board">

  <div class="page-title"><span>HOME</span></div>

  <section class="screen screen--inactive" aria-label="Home page, button at rest">
    <div class="screen__glow"></div>
    <header>
      <div class="brand"><span class="brand__mark"></span><span class="brand__name">veltraxa</span></div>
      <nav class="nav"><a class="nav__link" href="#">ABOUT US</a><a class="nav__link" href="#">CONTACT US</a></nav>
    </header>
    <div class="hero">
      <h1 class="hero__title">FIRE ENGINEERING</h1>
      <p class="hero__subtitle">THOUGHTFUL, RESPONSIVE</p>
      <a class="hero__cta" href="#">CONTACT US NOW</a>
    </div>
    <p class="tagline">We are a consulting fire engineers based in Wellington, New Zealand</p>
    <footer class="site-footer">
      <p class="site-footer__legal"><em>Copyright © 2017 Veltraxa.</em> Use of this website constitutes acceptance of our <a href="#">User Agreement and Privacy Policy.</a></p>
      <div class="social">
        <p class="social__caption">Follow and Like us at</p>
        <ul class="social__list">
          <li class="social__item" aria-label="Social link 1"></li>
          <li class="social__item" aria-label="Social link 2"></li>
          <li class="social__item" aria-label="Social link 3"></li>
          <li class="social__item" aria-label="Social link 4"></li>
        </ul>
      </div>
    </footer>
  </section>

  <p class="state-label state-label--inactive">INACTIVE</p>

  <section class="screen screen--active" aria-label="Home page, button hovered">
    <div class="screen__glow"></div>
    <header>
      <div class="brand"><span class="brand__mark"></span><span class="brand__name">veltraxa</span></div>
      <nav class="nav"><a class="nav__link" href="#">ABOUT US</a><a class="nav__link" href="#">CONTACT US</a></nav>
    </header>
    <div class="hero">
      <h1 class="hero__title">FIRE ENGINEERING</h1>
      <p class="hero__subtitle">THOUGHTFUL, RESPONSIVE</p>
      <a class="hero__cta" href="#">CONTACT US NOW
        <svg class="hero__pointer" viewBox="0 0 12 16" aria-hidden="true"><path d="M1 1 L1 13 L4 10 L6.5 15 L8.5 14 L6 9 L10.5 9 Z" fill="#ffffff" stroke="#000000" stroke-width="1"/></svg>
      </a>
    </div>
    <p class="tagline">We are a consulting fire engineers based in Wellington, New Zealand</p>
    <footer class="site-footer">
      <p class="site-footer__legal"><em>Copyright © 2017 Veltraxa.</em> Use of this website constitutes acceptance of our <a href="#">User Agreement and Privacy Policy.</a></p>
      <div class="social">
        <p class="social__caption">Follow and Like us at</p>
        <ul class="social__list">
          <li class="social__item" aria-label="Social link 1"></li>
          <li class="social__item" aria-label="Social link 2"></li>
          <li class="social__item" aria-label="Social link 3"></li>
          <li class="social__item" aria-label="Social link 4"></li>
        </ul>
      </div>
    </footer>
  </section>

  <p class="state-label state-label--active">ACTIVE</p>

</main>
</body>
</html>
```